Business card and stationery concept for weight management and nutrition practice
trueLeaf Guidance
Dear Designers,
I have uploaded my logo files and am looking forward to everyone's designs.
I would like to see designs that do not feature my logo quite so prominently - that is, the logo does not have to be very large.
Also, instead of bold abstract curves and shapes I'd like to see accents that are more feminine.
Thanks everyone!
I like the bold concepts you have uploaded. I would also like to see more simple ideas, using the light blue and dark grey used in the logo rather than black.
I would also like to see a few concepts that are a bit more feminine. Not overtly so but subtle.
Thank you!
I am unable to upload my logo at this time -- I will do this on Saturday evening when I get back in town.

```html
<!DOCTYPE html>
<html lang="en">
<head>
<meta charset="utf-8">
<title>trueLeaf Guidance – Business Card</title>
<link rel="stylesheet" href="https://fonts.googleapis.com/css2?family=Montserrat:wght@500;600&family=Open+Sans:wght@400;600&display=swap">
<style>
  :root {
    --page-bg: #e6e8ea;
    --card-white: #ffffff;
    --slate: #4b4d50;
    --slate-light: #606265;
    --sky: #8fb6d5;
    --sky-deep: #6f9cc0;
    --ink: #3f4144;
    --paper-text: #f2f3f4;
  }
  * { box-sizing: border-box; margin: 0; padding: 0; }
  html, body {
    width: 1200px; height: 1009px; overflow: hidden;
    background: var(--page-bg);
  }
  .sheet {
    width: 1200px; height: 1009px;
    display: flex; flex-direction: column; align-items: center; justify-content: center;
    gap: 40px;
  }
  .card {
    position: relative;
    width: 780px; height: 446px;
    background: var(--card-white);
    border-radius: 26px;
    overflow: hidden;
    box-shadow: 0 6px 18px rgba(0,0,0,0.12);
  }
  .wordmark {
    display: flex; align-items: center; gap: 12px;
    font-family: "Montserrat", sans-serif;
    font-weight: 600;
    color: var(--ink);
    white-space: nowrap;
  }
  .wordmark-dot {
    width: 18px; height: 18px; border-radius: 50%;
    background: var(--sky-deep);
    flex: none;
  }
  .card-front .wordmark {
    position: absolute; left: 50%; top: 50%;
    transform: translate(-50%, -50%);
    font-size: 40px;
  }
  .card-back .swoosh {
    position: absolute; inset: 0;
    width: 100%; height: 100%;
  }
  .card-back .wordmark {
    position: absolute; right: 48px; top: 100px;
    font-size: 32px;
  }
  .card-back .wordmark .wordmark-dot { width: 16px; height: 16px; }
  .contact-list {
    position: absolute; left: 28px; top: 150px;
    list-style: none;
    font-family: "Open Sans", sans-serif;
    font-size: 12.5px;
    color: var(--paper-text);
    display: flex; flex-direction: column; gap: 7px;
  }
  .contact-list li { display: flex; align-items: center; gap: 8px; }
  .contact-list svg { width: 15px; height: 15px; flex: none; }
  .signature {
    position: absolute; right: 34px; bottom: 22px;
    text-align: right;
    font-family: "Open Sans", sans-serif;
    color: var(--paper-text);
  }
  .signature .person { font-size: 14px; font-weight: 600; }
  .signature .role { font-size: 12px; margin-top: 2px; }
</style>
</head>
<body>
<main class="sheet">

  <section class="card card-front" aria-label="Card front">
    <div class="wordmark"><span class="wordmark-dot"></span>trueLeaf Guidance</div>
  </section>

  <section class="card card-back" aria-label="Card back">
    <svg class="swoosh" viewBox="0 0 780 446" preserveAspectRatio="none" aria-hidden="true">
      <defs>
        <linearGradient id="slateFill" x1="0" y1="0" x2="1" y2="1">
          <stop offset="0" stop-color="#5c5e61"/>
          <stop offset="1" stop-color="#45474a"/>
        </linearGradient>
      </defs>
      <path d="M0 0 H170 C260 190 470 330 780 368 V446 H0 Z" fill="url(#slateFill)"/>
      <path d="M170 0 C260 190 470 330 780 368" fill="none" stroke="#8fb6d5" stroke-width="26" transform="translate(14 -14)"/>
      <path d="M170 0 C260 190 470 330 780 368" fill="none" stroke="#ffffff" stroke-width="4" transform="translate(2 -3)"/>
      <path d="M170 0 C260 190 470 330 780 368" fill="none" stroke="#6f9cc0" stroke-width="3" transform="translate(36 -34)"/>
    </svg>

    <ul class="contact-list">
      <li>
        <svg viewBox="0 0 16 16" aria-hidden="true"><circle cx="8" cy="8" r="7.5" fill="#f2f3f4"/><path d="M8 3.5a2.6 2.6 0 0 0-2.6 2.6C5.4 8 8 12 8 12s2.6-4 2.6-5.9A2.6 2.6 0 0 0 8 3.5z" fill="#4b4d50"/></svg>
        418 North Alder Row
      </li>
      <li style="padding-left:23px">Brookvale, Ohio 43210</li>
      <li>
        <svg viewBox="0 0 16 16" aria-hidden="true"><circle cx="8" cy="8" r="7.5" fill="#f2f3f4"/><rect x="4" y="5" width="8" height="6" fill="none" stroke="#4b4d50" stroke-width="1.2"/><path d="M4 5l4 3.2L12 5" fill="none" stroke="#4b4d50" stroke-width="1.2"/></svg>
        hello@trueleafguidance.com
      </li>
      <li>
        <svg viewBox="0 0 16 16" aria-hidden="true"><circle cx="8" cy="8" r="7.5" fill="#f2f3f4"/><circle cx="8" cy="8" r="4" fill="none" stroke="#4b4d50" stroke-width="1.1"/><path d="M4 8h8M8 4c-1.6 2.4-1.6 5.6 0 8M8 4c1.6 2.4 1.6 5.6 0 8" fill="none" stroke="#4b4d50" stroke-width="1"/></svg>
        www.trueleafguidance.com
      </li>
    </ul>

    <div class="wordmark"><span class="wordmark-dot"></span>trueLeaf Guidance</div>

    <div class="signature">
      <p class="person">Nora J. Whitfield, MS, RD, LDN</p>
      <p class="role">Registered Dietitian</p>
    </div>
  </section>

</main>
</body>
</html>
```